Doctors clinic requires stationary designed

We require various types of stationary to be design based on the logo (attached). We require the following:
- Letterhead (A4 Portrait)
- Business Card (must include UV spot on rear)
- With compliments slip (DL Landscape)
- Appointments card (Folded A6)

We are a young clinical practice which boasts a modern and sophisticated approach to medicine so we require something which feels fresh and modern. Please include colours represented in the logo (contrasting teal and grey). We are calling for creative minds to put forth their ideas and we will be actively providing feedback on all designs.

thank you

Clinic

```html
<!DOCTYPE html>
<html lang="en">
<head>
<meta charset="utf-8">
<title>Dr Clara Wendell – Business Card</title>
<link rel="stylesheet" href="https://fonts.googleapis.com/css2?family=Open+Sans:wght@300;400;700&display=swap">
<style>
  :root {
    --teal: #0e7a70;
    --green: #6aae7e;
    --grey-text: #4a4a4a;
    --card: #f7f7f7;
    --backdrop: #9a9a9a;
  }
  * { box-sizing: border-box; margin: 0; padding: 0; }
  html, body { width: 1200px; height: 720px; overflow: hidden; }
  body {
    background: var(--backdrop);
    font-family: "Open Sans", Arial, sans-serif;
    position: relative;
  }
  .card {
    position: absolute;
    top: 206px;
    width: 540px;
    height: 308px;
    background: var(--card);
    box-shadow: 0 4px 14px rgba(0,0,0,0.18);
    overflow: hidden;
  }
  .card--front { left: 40px; }
  .card--back  { left: 620px; }
  .card__bands { position: absolute; inset: 0; }

  .brand {
    position: absolute;
    display: flex;
    align-items: center;
    gap: 12px;
  }
  .card--front .brand { left: 150px; top: 48px; }
  .card--back .brand { left: 36px; top: 58px; }
  .brand__dot {
    width: 34px; height: 34px;
    border: 2px solid var(--teal);
    border-radius: 50%;
    flex: none;
  }
  .brand__name {
    color: var(--teal);
    font-weight: 700;
    font-size: 22px;
    line-height: 1.05;
  }
  .card--back .brand__name { font-size: 18px; }
  .brand__tagline {
    color: var(--teal);
    font-weight: 400;
    font-size: 11.5px;
    margin-top: 3px;
  }
  .card--back .brand__tagline { font-size: 10px; }

  .holder {
    position: absolute;
    left: 38px; top: 150px;
  }
  .holder__name { color: var(--teal); font-weight: 700; font-size: 16px; }
  .holder__role { color: var(--grey-text); font-weight: 300; font-size: 13px; }

  .divider {
    position: absolute;
    left: 262px; top: 162px;
    width: 16px; height: 74px;
    background: linear-gradient(90deg, rgba(0,0,0,0.08), rgba(0,0,0,0));
  }

  .contact {
    position: absolute;
    left: 300px; top: 164px;
    list-style: none;
    color: var(--grey-text);
    font-weight: 300;
    font-size: 12.5px;
    line-height: 16px;
  }
  .contact li { display: flex; gap: 10px; align-items: flex-start; }
  .contact svg { width: 11px; height: 12px; margin-top: 2px; flex: none; }
  .contact li.no-icon { padding-left: 21px; }

  .pattern-area {
    position: absolute;
    right: 0; top: 0;
    width: 300px; height: 308px;
    background: radial-gradient(circle at 65% 50%, rgba(14,122,112,0.35), rgba(14,122,112,0.08) 65%, rgba(14,122,112,0) 80%);
  }
</style>
</head>
<body>

<section class="card card--front" aria-label="Business card front">
  <svg class="card__bands" viewBox="0 0 540 308" aria-hidden="true">
    <defs>
      <linearGradient id="greenBand" x1="0" x2="1">
        <stop offset="0" stop-color="#7bbb8c"/>
        <stop offset="1" stop-color="#5fa274"/>
      </linearGradient>
    </defs>
    <polygon points="0,252 274,252 290,270 0,270" fill="var(--teal)"/>
    <polygon points="292,252 540,252 540,276 312,276" fill="url(#greenBand)"/>
  </svg>

  <div class="brand">
    <span class="brand__dot"></span>
    <div>
      <div class="brand__name">Dr Clara Wendell</div>
      <div class="brand__tagline">Obstetrician and Gynaecologist</div>
    </div>
  </div>

  <div class="holder">
    <div class="holder__name">Dr. Clara Wendell</div>
    <div class="holder__role">Medical Director</div>
  </div>

  <div class="divider"></div>

  <ul class="contact">
    <li>
      <svg viewBox="0 0 11 12"><path d="M5.5 0a4 4 0 0 0-4 4c0 3 4 8 4 8s4-5 4-8a4 4 0 0 0-4-4zm0 5.5a1.5 1.5 0 1 1 0-3 1.5 1.5 0 0 1 0 3z" fill="var(--teal)"/></svg>
      <span>14 Linden Row</span>
    </li>
    <li class="no-icon">Ashford Vale 4821K</li>
    <li>
      <svg viewBox="0 0 11 12"><rect x="1" y="1.5" width="9" height="9" rx="1" fill="none" stroke="var(--teal)" stroke-width="1.4"/></svg>
      <span>0555 987 2103</span>
    </li>
    <li>
      <svg viewBox="0 0 11 12"><rect x="3" y="0.5" width="5" height="4" fill="var(--teal)"/><rect x="0.5" y="4" width="10" height="5" rx="1" fill="var(--teal)"/><rect x="3" y="8" width="5" height="3.5" fill="var(--teal)"/></svg>
      <span>(086) 410 2298</span>
    </li>
    <li>
      <svg viewBox="0 0 11 12"><rect x="0.5" y="2.5" width="10" height="7" fill="var(--teal)"/><path d="M0.5 2.5l5 4 5-4" fill="none" stroke="#fff" stroke-width="1"/></svg>
      <span>name@drclarawendell.com</span>
    </li>
  </ul>
</section>

<section class="card card--back" aria-label="Business card back">
  <div class="pattern-area" role="img" aria-label="Large spot-UV decorative pattern in teal"></div>

  <div class="brand">
    <span class="brand__dot"></span>
    <div>
      <div class="brand__name">Dr Clara Wendell</div>
      <div class="brand__tagline">Obstetrician and Gynaecologist</div>
    </div>
  </div>
</section>

</body>
</html>
```